Fresh & Clean *NEW* BUSINESS CARD Needed - OPTOMETRY Clinic/Optical

High-tech optometry practice with 3 doctors seeking new business card.  We provide eye exams, sell, designer glasses/contacts/specialty eyewear and treat ocular diseases.  For our business cards, we are seeking fresh, clean, and crisp design as we grow our team (staffing change).  Simply adding doctors is making the card look busy/cluttered.
 Looking for professional, less cluttered look yet still have our logo, doctor names, phone, address, and website....If possible!  :)
Names:
Marcia Trelford, O.D.
Ned Pallister, O.D.
Oona Ferrant, O.D.
Phone: 555-014-2738
Website: www.BrightLensHub.example
Address:  417 Garnet R. Holloway, Lindenvale, ZZ 00000
Ultimately we have the main business card with all doctor sames and that card has two versions  (front is always the same).  The back has two designs (1) displays next appointment time/date, (2) for "general use" (non-appointment.)    I have attached what we have used in the past.  
We also need a design template for each team member in our practice with their name, title, and email.   Those should be designed with the "general use" back (see attached).
**Open to entirely new design so don't feel obligated to keep current format.  Need new perspective!  Also including our watermark and some other design features we have consistently used in past in our portfolio.  Included are two options for logos--vertical and horizontal.
**I also would like to remove "Member of Sight Alliance" on our logo if possible**
 Other image files available upon request.

Target Market(s)

New patient & Current Patients

Industry/Entity Type

Optometry

Contact Information for Business Card

High-tech optometry practice with 3 doctors seeking new business card.  We provide eye exams, sell, designer glasses/contacts/specialty eyewear and treat ocular diseases.  For our business cards, we are seeking fresh, clean, and crisp design as we grow our team (staffing change).  Simply adding doctors is making the card look busy/cluttered.  Looking for professional, less cluttered look yet still have our logo, doctor names, phone, address, and website....If possible!  :) Names: Marcia Trelford, O.D. Ned Pallister, O.D. Oona Ferrant, O.D. Phone: 555-014-2738 Website: www.BrightLensHub.example Address:  417 Garnet R. Holloway, Lindenvale, ZZ 00000 Ultimately we have the main business card with all doctor sames and that card has two versions  (front is always the same).  The back has two designs (1) displays next appointment time/date, (2) for "general use" (non-appointment.)    I have attached what we have used in the past.   We also need a design template for each team member in our practice with their name, title, and email.   Those should be designed with the "general use" back (see attached). **Open to entirely new design so don't feel obligated to keep current format.  Need new perspective!  Also including our watermark and some other design features we have consistently used in past in our portfolio.  Included are two options for logos--vertical and horizontal. **I also would like to remove "Member of Sight Alliance" on our logo if possible**  Other image files available upon request.

Font styles to use
Other font styles liked:
• We have used Montserrat / Yellowtail in the past

Colors

Designer to choose colors to be used in the design.

Requirements
Must have
• Clean & Fresh Design with Logo / Info provided in description. Horizontal orientation. **I have included the CMYK colors we currently have in our logo.
Should not have
• Cluttered

```html
<!DOCTYPE html>
<html lang="en">
<head>
<meta charset="utf-8">
<title>Bright Lens Hub – Business Card</title>
<link rel="stylesheet" href="https://fonts.googleapis.com/css2?family=Questrial&family=Mulish:wght@400;700&family=Yellowtail&display=swap">
<style>
  :root {
    --backdrop: #b3b3b3;
    --slate: #6c6d70;
    --ink: #6b6b6b;
    --ink-soft: #777;
    --gold: #d4a917;
    --aqua: #93b0b6;
    --aqua-icon: #9fd3de;
    --paper: #ffffff;
    --rule: #8a8a8a;
  }
  * { box-sizing: border-box; margin: 0; padding: 0; }
  html, body { width: 1200px; height: 1000px; overflow: hidden; }
  body { background: var(--backdrop); position: relative; font-family: "Mulish", sans-serif; }

  .card {
    position: absolute; left: 315px; width: 570px; height: 328px;
    border-radius: 26px; overflow: hidden;
  }
  .card--front { top: 148px; background: var(--slate); }
  .card--back  { top: 527px; background: var(--paper); }

  /* front */
  .front-glow {
    position: absolute; left: 300px; top: 20px; width: 310px; height: 300px;
    border-radius: 50%;
    background: radial-gradient(circle at 50% 50%, var(--aqua) 0%, var(--aqua) 45%, rgba(147,176,182,0.35) 62%, rgba(108,109,112,0) 72%);
  }
  .front-name {
    position: absolute; left: 38px; top: 150px;
    font-family: "Questrial", sans-serif; font-size: 48px; line-height: 52px;
    color: var(--paper); letter-spacing: 1px; white-space: nowrap;
  }
  .front-name span { display: block; }
  .front-name .front-name-second { padding-left: 28px; }
  .front-web {
    position: absolute; left: 37px; top: 262px;
    font-family: "Mulish", sans-serif; font-weight: 700; font-size: 19px; color: var(--paper);
  }

  /* back – left column */
  .doctors {
    position: absolute; left: 42px; top: 66px;
    font-family: "Yellowtail", cursive; color: var(--gold);
    font-size: 28px; line-height: 34px; list-style: none; white-space: nowrap;
  }
  .contact { position: absolute; left: 37px; top: 186px; color: var(--ink-soft); }
  .contact-row { display: flex; align-items: center; gap: 7px; height: 24px; }
  .contact-row svg { flex: none; }
  .contact-phone { font-size: 18px; }
  .contact-web { font-size: 14.5px; }
  .divider { position: absolute; left: 42px; top: 250px; width: 168px; height: 1px; background: var(--rule); }
  .address { position: absolute; left: 41px; top: 259px; font-size: 14.5px; line-height: 18px; color: var(--ink-soft); font-style: normal; }

  /* back – appointment column */
  .appt-field { position: absolute; left: 301px; width: 226px; height: 30px; }
  .appt-field--date { top: 64px; }
  .appt-field--time { top: 103px; }
  .appt-label { position: absolute; left: 0; bottom: 2px; font-weight: 700; font-size: 20px; color: var(--ink-soft); }
  .appt-line { position: absolute; left: 49px; right: 0; bottom: 6px; height: 1px; background: var(--rule); }
  .appt-sep { position: absolute; left: 125px; bottom: 6px; font-size: 16px; color: var(--ink-soft); }
  .days { position: absolute; left: 301px; top: 154px; display: flex; gap: 19.5px; list-style: none; }
  .days li {
    width: 21px; height: 21px; border: 1px solid var(--ink-soft);
    font-size: 12px; color: var(--ink-soft); display: flex; align-items: center; justify-content: center;
  }
  .notice { position: absolute; left: 296px; width: 236px; top: 198px; text-align: center; font-size: 12px; line-height: 15px; color: var(--ink-soft); }
  .brand { position: absolute; left: 303px; top: 260px; display: flex; align-items: center; gap: 8px; }
  .brand-dot { width: 28px; height: 28px; border-radius: 50%; background: var(--aqua-icon); }
  .brand-name { font-family: "Questrial", sans-serif; font-size: 24px; color: var(--ink); letter-spacing: 0.5px; }
</style>
</head>
<body>
  <section class="card card--front" aria-label="Card front">
    <div class="front-glow" role="img" aria-label="Soft aqua glow decoration"></div>
    <p class="front-name"><span>Bright Lens</span><span class="front-name-second">Hub</span></p>
    <p class="front-web">BrightLensHub.example</p>
  </section>

  <section class="card card--back" aria-label="Card back, appointment version">
    <ul class="doctors">
      <li>Marcia Trelford, O.D.</li>
      <li>Ned Pallister, O.D.</li>
      <li>Oona Ferrant, O.D.</li>
    </ul>

    <div class="contact">
      <p class="contact-row contact-phone">
        <svg width="20" height="20" viewBox="0 0 20 20" aria-hidden="true">
          <circle cx="10" cy="10" r="10" fill="var(--aqua-icon)"/>
          <path d="M7 5.5c.6-.3 1 .1 1.3.6l.8 1.5c.2.4 0 .8-.3 1.1l-.5.4c.5 1.1 1.3 1.9 2.4 2.4l.4-.5c.3-.3.7-.5 1.1-.3l1.5.8c.5.3.9.7.6 1.3-.4.9-1.4 1.4-2.4 1.1-2.6-.8-4.6-2.8-5.4-5.4-.3-1 .2-2 1-2.4z" fill="var(--ink)"/>
        </svg>
        (555) 014-2738
      </p>
      <p class="contact-row contact-web">
        <svg width="20" height="20" viewBox="0 0 20 20" aria-hidden="true">
          <circle cx="10" cy="10" r="10" fill="var(--aqua-icon)"/>
          <g fill="none" stroke="var(--ink)" stroke-width="0.9">
            <circle cx="10" cy="10" r="5"/>
            <ellipse cx="10" cy="10" rx="2.2" ry="5"/>
            <line x1="5" y1="10" x2="15" y2="10"/>
            <line x1="5.8" y1="7.5" x2="14.2" y2="7.5"/>
            <line x1="5.8" y1="12.5" x2="14.2" y2="12.5"/>
          </g>
        </svg>
        &nbsp;BrightLensHub.example
      </p>
    </div>
    <div class="divider"></div>
    <address class="address">417 Garnet R. Holloway,<br>Lindenvale, ZZ 00000</address>

    <div class="appt-field appt-field--date">
      <span class="appt-label">Date</span><span class="appt-line"></span><span class="appt-sep">/</span>
    </div>
    <div class="appt-field appt-field--time">
      <span class="appt-label">Time</span><span class="appt-line"></span><span class="appt-sep">:</span>
    </div>
    <ul class="days">
      <li>M</li><li>T</li><li>W</li><li>T</li><li>F</li><li>S</li>
    </ul>
    <p class="notice">If your unable to keep your appointment,<br>kindly give us 34 hour notice</p>

    <div class="brand">
      <span class="brand-dot"></span>
      <span class="brand-name">Bright Lens Hub</span>
    </div>
  </section>
</body>
</html>
```